Design My Bussiness Card
Technology company
Project: Design My Bussiness Card
Design My Bussiness Card -
Creative Brief
Professional
Dorian Pelkey
2847 E. Tollbrook #3
marisa@vantrelo.net
www.qoribelix.info

```html
<!DOCTYPE html>
<html lang="en">
<head>
<meta charset="utf-8">
<title>Qoribelix Stationery</title>
<link href="https://fonts.googleapis.com/css2?family=Arimo:wght@400;700&display=swap" rel="stylesheet">
<style>
:root{
  --green-dark:#0f6a2c;
  --green:#1f8a3a;
  --green-light:#cfe8c6;
  --green-pale:#eef6ea;
  --ink:#3a3a3a;
  --paper:#ffffff;
  --frame:#d9d9d9;
}
*{box-sizing:border-box;margin:0;padding:0}
html,body{width:1200px;height:722px;overflow:hidden;background:#fff;font-family:"Arimo",Arial,sans-serif;color:var(--ink)}
.sheet{position:absolute;left:10px;top:8px;width:1180px;height:704px;border:1px solid var(--frame);border-radius:6px;background:var(--paper);box-shadow:0 1px 4px rgba(0,0,0,.15)}
.piece{position:absolute;background:var(--paper);box-shadow:0 2px 6px rgba(0,0,0,.22);overflow:hidden}
.piece svg.bg{position:absolute;left:0;top:0}
.brand{position:absolute;display:flex;align-items:center;gap:8px;white-space:nowrap}
.brand-dot{border-radius:50%;background:var(--green);flex:none}
.brand-name{font-weight:700;color:var(--green-dark);letter-spacing:.5px}
.brand-tag{position:absolute;font-size:6px;color:var(--green);letter-spacing:.3px;white-space:nowrap}
.person{position:absolute;color:var(--green);font-size:15px;white-space:nowrap}
.contacts{position:absolute;font-size:8px;line-height:12px;color:var(--ink);white-space:nowrap}
.contacts b{display:inline-block;width:14px;color:var(--green-dark)}
.faint-mark{position:absolute;border-radius:50%;border:34px solid var(--green-light);opacity:.6}

.card-front{left:55px;top:48px;width:345px;height:194px}
.card-back{left:55px;top:242px;width:345px;height:206px;background:linear-gradient(180deg,var(--green-pale),#d7ecd0 60%,#f4faf1)}
.letterhead{left:416px;top:48px;width:460px;height:601px}
.envelope{left:574px;top:182px;width:576px;height:338px}
</style>
</head>
<body>
<div class="sheet"></div>

<!-- business card front -->
<div class="piece card-front">
  <svg class="bg" width="345" height="194" viewBox="0 0 345 194">
    <rect x="0" y="0" width="44" height="194" fill="var(--green)"/>
    <path d="M44 0 H74 C40 50 40 144 74 194 H44 Z" fill="var(--green-dark)"/>
    <path d="M74 0 C40 50 40 144 74 194 H96 C62 144 62 50 96 0 Z" fill="var(--green-light)" opacity=".8"/>
  </svg>
  <div class="person" style="right:14px;top:10px">Dorian Pelkey</div>
  <div class="brand" style="left:100px;top:46px">
    <span class="brand-dot" style="width:22px;height:22px"></span>
    <span class="brand-name" style="font-size:22px">QORIBELIX</span>
  </div>
  <div class="brand-tag" style="left:130px;top:72px">Professional Tech Solutions</div>
  <div class="contacts" style="left:170px;top:116px">
    <div><b>P</b>5550184273</div>
    <div><b>C</b>5550184273</div>
    <div><b>E</b>marisa@vantrelo.net</div>
    <div><b>W</b>www.qoribelix.info</div>
  </div>
</div>

<!-- business card back -->
<div class="piece card-back">
  <div class="brand" style="left:14px;top:90px">
    <span class="brand-dot" style="width:26px;height:26px"></span>
    <span class="brand-name" style="font-size:24px">QORIBELIX</span>
  </div>
  <div class="brand-tag" style="left:60px;top:120px">Professional Tech Solutions</div>
</div>

<!-- letterhead -->
<div class="piece letterhead">
  <svg class="bg" width="460" height="601" viewBox="0 0 460 601">
    <path d="M0 0 H60 C22 80 16 200 24 601 H0 Z" fill="var(--green)"/>
    <path d="M60 0 H80 C40 80 30 200 28 601 H24 C16 200 22 80 60 0 Z" fill="var(--green-light)"/>
  </svg>
  <div class="brand" style="left:58px;top:40px">
    <span class="brand-dot" style="width:22px;height:22px"></span>
    <span class="brand-name" style="font-size:20px">QORIBELIX</span>
  </div>
  <div class="brand-tag" style="left:88px;top:65px">Professional Tech Solutions</div>
  <div class="person" style="right:18px;top:44px">Dorian Pelkey</div>
  <div class="faint-mark" style="left:300px;top:420px;width:150px;height:150px"></div>
  <div class="contacts" style="left:34px;top:548px">
    <div><b>P</b>5550184273</div>
    <div><b>C</b>5550184273</div>
    <div><b>E</b>marisa@vantrelo.net</div>
    <div><b>W</b>www.qoribelix.info</div>
  </div>
</div>

<!-- envelope -->
<div class="piece envelope">
  <svg class="bg" width="576" height="338" viewBox="0 0 576 338">
    <rect x="0" y="0" width="14" height="338" fill="var(--green)"/>
    <path d="M14 0 H60 C24 60 22 200 14 338 Z" fill="var(--green-light)" opacity=".8"/>
  </svg>
  <div class="brand" style="left:40px;top:36px">
    <span class="brand-dot" style="width:22px;height:22px"></span>
    <span class="brand-name" style="font-size:20px">QORIBELIX</span>
  </div>
  <div class="brand-tag" style="left:70px;top:61px">Professional Tech Solutions</div>
  <div class="faint-mark" style="left:390px;top:130px;width:170px;height:170px"></div>
  <div class="contacts" style="left:26px;top:264px">
    <div><b>P</b>5550184273</div>
    <div><b>C</b>5550184273</div>
    <div><b>E</b>marisa@vantrelo.net</div>
    <div><b>W</b>www.qoribelix.info</div>
  </div>
</div>
</body>
</html>
```